Lanternleaf take out menu

We need a take out menu design using our menu attached. Info to include would be our address: 7816 Brindlewood Hollow Pkwy #204, Bellcrest, LA 70599. Phone number is 337-514-2960. website is www.lanternleafgrv.com.

Industry/Entity Type

Asian Restaurant

```html
<!DOCTYPE html>
<html lang="en">
<head>
<meta charset="utf-8">
<title>Lanternleaf Take Out Menu</title>
<link href="https://fonts.googleapis.com/css2?family=Patrick+Hand&display=swap" rel="stylesheet">
<style>
:root{
  --bg:#f4f2f1;
  --paper:#ece9e8;
  --paper-shade:#e4e0df;
  --red:#9a3a3f;
  --red-deep:#7e2a30;
  --ink:#4a4646;
  --rule:#c9a6a8;
  --chili:#c0262d;
}
*{box-sizing:border-box;margin:0;padding:0}
html,body{width:1200px;height:900px;overflow:hidden;background:var(--bg)}
body{font-family:"Patrick Hand",cursive;color:var(--ink)}
.spread{position:absolute;top:237px;width:585px;height:425px;display:flex;box-shadow:0 2px 10px rgba(0,0,0,.12)}
.spread.outside{left:5px}
.spread.inside{left:610px}
.panel{width:195px;height:425px;background:var(--paper);border-top:2px solid var(--red);padding:8px 9px;position:relative;overflow:hidden}
.panel:nth-child(2){background:var(--paper-shade)}
.h-section{color:var(--red);text-align:center;font-size:9px;font-weight:normal;letter-spacing:.8px;text-transform:uppercase;margin:3px 0 2px}
.h-sub{text-align:center;font-size:6px;font-weight:normal;letter-spacing:.6px;text-transform:uppercase;margin:2px 0 1px}
.item{display:flex;justify-content:space-between;border-bottom:.5px solid var(--rule);padding:1.2px 0;line-height:1.12}
.item .txt{flex:1;padding-right:4px}
.item .name{color:var(--red);font-size:5.4px;display:block}
.item .desc{font-size:4.6px;display:block}
.item .price{font-size:4.8px}
.hot{display:inline-block;width:4px;height:2px;border-radius:2px;background:var(--chili);margin-left:1px;vertical-align:middle}
.compact .item{padding:.8px 0}
.compact .item .name{font-size:5px}
.compact .item .desc{font-size:4.3px}
.story p{font-size:5.3px;line-height:1.3;text-align:justify;margin-bottom:1px}
.badge{width:84px;height:84px;border:3px solid var(--red);border-radius:50%;margin:16px auto 0;display:flex;align-items:center;justify-content:center;color:var(--red);font-size:13px}
.contact{position:absolute;left:0;right:0;bottom:22px;text-align:center;font-size:5.6px;line-height:2.1}
.contact svg{width:6px;height:6px;vertical-align:middle;margin-right:3px;fill:var(--red)}
.brand{display:flex;align-items:center;justify-content:center;gap:4px;color:var(--red-deep);font-size:22px;line-height:1}
.brand .dot{width:11px;height:11px;border-radius:50%;background:var(--red)}
.brand-tag{text-align:center;font-size:5px;letter-spacing:1.4px;text-transform:uppercase;margin-top:2px}
.cover .brand-block{margin-top:95px}
.takeout{margin-top:38px;border-top:.6px solid var(--rule);border-bottom:.6px solid var(--rule);padding:14px 0;text-align:center;font-size:10px}
.art{position:absolute;left:25px;right:20px;top:235px;height:170px;background:linear-gradient(135deg,rgba(60,40,40,.05),rgba(154,58,63,.18) 60%,rgba(192,38,45,.25));border-radius:3px}
.inside .brand{font-size:18px}
.inside .brand .dot{width:9px;height:9px}
.bar-cols{display:flex;gap:3px;font-size:4.3px;line-height:1.25}
.bar-cols div{flex:1}
.bar-cols b{display:block;color:var(--red);font-weight:normal;font-size:4.6px}
</style>
</head>
<body>

<section class="spread outside">
  <div class="panel appetizers">
    <h2 class="h-section">Appetizers</h2>
    <div class="item"><span class="txt"><span class="name">Edamame</span><span class="desc">Seasoned &amp; boiled soy bean</span></span><span class="price">$6</span></div>
    <div class="item"><span class="txt"><span class="name">Scallion Pancakes</span><span class="desc">Traditional Chinese flatbread folded with oil and minced scallions, pan fried</span></span><span class="price">$8</span></div>
    <div class="item"><span class="txt"><span class="name">Lanternleaf Lettuce Wraps</span><span class="desc">Seasoned ground chicken drizzled with our secret sauce, served with lettuce</span></span><span class="price">$13</span></div>
    <div class="item"><span class="txt"><span class="name">Salt &amp; Pepper Calamari</span><span class="desc">Crispy calamari with green &amp; red peppers and onions</span></span><span class="price">$13</span></div>
    <div class="item"><span class="txt"><span class="name">Bang Bang Shrimp</span><span class="desc">Crispy fried shrimp tossed in our creamy spicy sauce</span></span><span class="price">$14</span></div>
    <div class="item"><span class="txt"><span class="name">Drunken Chicken <i class="hot"></i></span><span class="desc">Chicken, Thai chili in a house made spicy sauce</span></span><span class="price">$14</span></div>
    <div class="item"><span class="txt"><span class="name">Sichuan Spiced Beef <i class="hot"></i><i class="hot"></i></span><span class="desc">Beef shank, beef tripe, cilantro, peanuts and celery</span></span><span class="price">$14</span></div>
    <div class="item"><span class="txt"><span class="name">Beef Crispy Bottom Bao</span><span class="desc">Pan fried crispy bottom bao stuffed with beef, scallion and sesame (takes at least 20 mins)</span></span><span class="price">$14</span></div>
    <div class="item"><span class="txt"><span class="name">Shrimp &amp; Beef Crispy Bottom Bao</span><span class="desc">Pan fried bao stuffed with beef and shrimp, scallion and sesame (at least 20 mins)</span></span><span class="price">$14</span></div>
    <div class="item"><span class="txt"><span class="name">Crispy Mala Beef Jerky <i class="hot"></i><i class="hot"></i></span><span class="desc">Dry fried shredded beef with peppers in sesame and peppercorn oil</span></span><span class="price">$14</span></div>
    <div class="item"><span class="txt"><span class="name">Fried Chicken Dumplings (6)</span><span class="desc">Chinese dumpling stuffed with chicken, shiitake mushrooms and bamboo shoots</span></span><span class="price">$14</span></div>
    <div class="item"><span class="txt"><span class="name">Red Oil Dumplings (6) <i class="hot"></i></span><span class="desc">Pork filled dumplings in Sichuan red oil sauce drizzled with sesame</span></span><span class="price">$14</span></div>
    <div class="item"><span class="txt"><span class="name">Pork Egg Rolls (2)</span><span class="desc">Hand rolled with julienned veggies, sweet n' sour mustard sauce</span></span><span class="price">$14</span></div>
    <div class="item"><span class="txt"><span class="name">Vegetarian Spring Rolls (3)</span><span class="desc">Traditional Asian roll served with a sweet chili sauce</span></span><span class="price">$14</span></div>
    <div class="item"><span class="txt"><span class="name">Garlic Cucumber Salad</span><span class="desc">Sliced cucumber with a garlic vinaigrette</span></span><span class="price">$14</span></div>
    <div class="item"><span class="txt"><span class="name">Hot n' Sour Soup <i class="hot"></i></span><span class="desc">Tangy broth with bamboo shoot, wood ear fungus, tofu, egg and carrots</span></span><span class="price">$14</span></div>
    <div class="item"><span class="txt"><span class="name">West Lake Soup</span><span class="desc">Light creamy soup with ground beef, shiitake, tofu, bamboo, egg white, cilantro</span></span><span class="price">$14</span></div>
  </div>

  <div class="panel story">
    <h2 class="h-section">Our Story</h2>
    <p>At Lanternleaf we pride ourselves in serving fresh authentic Sichuan Chinese cuisine delicately prepared by our expertly trained chefs.</p>
    <p>Sichuan cuisine originates from southwest China between the Sichuan Basin and Tibetan Plateau. It is known for being both very spicy and flavorful, much like our own southern Louisiana cuisine.</p>
    <p>Our Executive Chef Wen Liang grew up in the southwestern Chinese province of Sichuan where he began his training at fifteen years old under his grandfather's mentorship. Chef Liang became an acclaimed chef in his province, opening several restaurants and traveling throughout China to cater for many of China's elite. His dream was to share his Sichuan style with the world, which lead him to the United States. He has worked in restaurants in both Houston and New York and we now welcome him to his new home in Bellcrest, Louisiana.</p>
    <p>We are very excited to bring to Bellcrest the authenticity of Chinese cuisine and hope you enjoy your experience dining with us.</p>
    <div class="badge">Lanternleaf</div>
    <div class="contact">
      <div><svg viewBox="0 0 10 10"><path d="M5 0a3.5 3.5 0 0 0-3.5 3.5C1.5 6 5 10 5 10s3.5-4 3.5-6.5A3.5 3.5 0 0 0 5 0zm0 5a1.5 1.5 0 1 1 0-3 1.5 1.5 0 0 1 0 3z"/></svg>7816 Brindlewood Hollow Pkwy #204, Bellcrest, LA 70599</div>
      <div><svg viewBox="0 0 10 10"><path d="M2 0.5l2 2-1 1.3c.6 1.3 1.6 2.3 2.9 2.9l1.3-1 2 2-1.2 1.8C4.7 9.3.7 5.3.4 1.7z"/></svg>337-514-2960</div>
      <div><svg viewBox="0 0 10 10"><circle cx="5" cy="5" r="4.2" fill="none" stroke="#9a3a3f" stroke-width="1"/><path d="M1 5h8M5 .8v8.4" stroke="#9a3a3f" stroke-width=".8"/></svg>www.lanternleafgrv.com</div>
    </div>
  </div>

  <div class="panel cover">
    <div class="brand-block">
      <div class="brand"><span class="dot"></span>Lanternleaf</div>
      <div class="brand-tag">Fresh Asian Cuisine</div>
    </div>
    <div class="takeout">Take out menu</div>
    <div class="art" role="img" aria-label="Illustration of a pair of red and black chopsticks holding a red chili pepper"></div>
  </div>
</section>

<section class="spread inside">
  <div class="panel entrees compact">
    <h2 class="h-section">Entrees</h2>
    <h3 class="h-sub">Chef Specialties</h3>
    <div class="item"><span class="txt"><span class="name">Jasmine Tea Smoked Duck</span><span class="desc">Boneless half duck with thinly sliced cucumber, scallion, duck sauce, soft flour wrap</span></span><span class="price">$24</span></div>
    <div class="item"><span class="txt"><span class="name">Sizzling Cumin Lamb <i class="hot"></i></span><span class="desc">Tender pieces of lamb rubbed in cumin, Sichuan peppers, celery and cilantro</span></span><span class="price">$16</span></div>
    <div class="item"><span class="txt"><span class="name">Chef Liang's Spicy Beef <i class="hot"></i><i class="hot"></i></span><span class="desc">Angus beef in green peppercorn sauce with Sichuan peppercorn, Thai chili, cilantro</span></span><span class="price">$16</span></div>
    <div class="item"><span class="txt"><span class="name">Chef Liang's Spicy Fish <i class="hot"></i><i class="hot"></i></span><span class="desc">Fish filet in green peppercorn sauce with Sichuan peppercorn, Thai chili, cilantro</span></span><span class="price">$17</span></div>
    <div class="item"><span class="txt"><span class="name">General Tso's Scallops <i class="hot"></i></span><span class="desc">Tender scallops marinated in a sweet chili sauce with broccoli and red peppers</span></span><span class="price">$18</span></div>
    <h3 class="h-sub">Beef &amp; Pork</h3>
    <div class="item"><span class="txt"><span class="name">Dancing Beef <i class="hot"></i><i class="hot"></i><i class="hot"></i></span><span class="desc">Angus beef slices on sizzling rice crackers, black peppercorn, Thai chili</span></span><span class="price">$16</span></div>
    <div class="item"><span class="txt"><span class="name">Oyster Beef</span><span class="desc">Tender cuts of steak wok fried and marinated in a homemade oyster sauce</span></span><span class="price">$14</span></div>
    <div class="item"><span class="txt"><span class="name">Double Pepper Beef <i class="hot"></i><i class="hot"></i><i class="hot"></i></span><span class="desc">Angus steak cubes with green peppercorn, Thai chili, serrano pepper, celery</span></span><span class="price">$16</span></div>
    <div class="item"><span class="txt"><span class="name">Black Pepper Steak</span><span class="desc">Tender cuts of steak mixed with onions and red and green bell peppers</span></span><span class="price">$15</span></div>
    <div class="item"><span class="txt"><span class="name">Singapore Baby Back Ribs</span><span class="desc">Tender baby back ribs rubbed in a Thai inspired sweet tangy glaze</span></span><span class="price">$16</span></div>
    <div class="item"><span class="txt"><span class="name">Dancing Pork Belly</span><span class="desc">Braised pork belly on sizzling rice cracker</span></span><span class="price">$15</span></div>
    <div class="item"><span class="txt"><span class="name">Twice Cooked Pork <i class="hot"></i></span><span class="desc">Stir fried pork belly slices with leek and fermented black beans</span></span><span class="price">$14</span></div>
    <h3 class="h-sub">Chicken</h3>
    <div class="item"><span class="txt"><span class="name">Kung Pao Chicken <i class="hot"></i></span><span class="desc">Chicken with roasted peanuts, scallions, dry red chili, Sichuan peppercorns</span></span><span class="price">$13</span></div>
    <div class="item"><span class="txt"><span class="name">Orange Chicken</span><span class="desc">Battered fried chicken breast with dried chili peppers in a tangy orange sauce</span></span><span class="price">$13</span></div>
    <div class="item"><span class="txt"><span class="name">Double Pepper Chicken <i class="hot"></i><i class="hot"></i><i class="hot"></i></span><span class="desc">Farm raised chicken with green peppercorn, Thai chili, serrano and jalapenos</span></span><span class="price">$13</span></div>
    <div class="item"><span class="txt"><span class="name">Crispy Spicy Chicken <i class="hot"></i></span><span class="desc">Crispy diced chicken with Sichuan peppers, cilantro and sesame</span></span><span class="price">$14</span></div>
    <div class="item"><span class="txt"><span class="name">General Tso's Chicken <i class="hot"></i></span><span class="desc">Battered fried chicken stir fried in a sweet &amp; tangy chili sauce</span></span><span class="price">$13</span></div>
    <div class="item"><span class="txt"><span class="name">Shredded Chicken in Spicy Garlic Sauce <i class="hot"></i></span><span class="desc">Shredded chicken, wood ear fungus, bamboo shoots in spicy garlic sauce</span></span><span class="price">$14</span></div>
    <div class="item"><span class="txt"><span class="name">Sweet &amp; Sour Chicken</span><span class="desc">Crispy chicken glazed in a homemade sweet &amp; sour marinade</span></span><span class="price">$13</span></div>
  </div>

  <div class="panel mains compact">
    <div class="brand"><span class="dot"></span>Lanternleaf</div>
    <div class="brand-tag">Fresh Asian Cuisine</div>
    <h2 class="h-section">Entrees</h2>
    <h3 class="h-sub">Seafood</h3>
    <div class="item"><span class="txt"><span class="name">Kung Pao Shrimp <i class="hot"></i></span><span class="desc">Shrimp with roasted peanuts, scallions, dry red chili, Sichuan peppercorns</span></span><span class="price">$16</span></div>
    <div class="item"><span class="txt"><span class="name">Rice Wine Shrimp &amp; Tofu <i class="hot"></i></span><span class="desc">Shrimp and tofu braised in garlic pickled pepper sauce with rice wine</span></span><span class="price">$18</span></div>
    <div class="item"><span class="txt"><span class="name">Shrimp in Spicy Garlic Sauce <i class="hot"></i></span><span class="desc">Shrimp with jicama, ginger, garlic and scallions in a spicy garlic sauce</span></span><span class="price">$15</span></div>
    <div class="item"><span class="txt"><span class="name">Lemon Peel Shrimp</span><span class="desc">Shrimp with fresh lemons in a sweet lemon sauce with vegetables</span></span><span class="price">$15</span></div>
    <div class="item"><span class="txt"><span class="name">Rice Wine Fish <i class="hot"></i></span><span class="desc">White fish filet braised in pickled pepper sauce with rice wine</span></span><span class="price">$14</span></div>
    <h2 class="h-section">Noodles &amp; Rice</h2>
    <div class="item"><span class="txt"><span class="name">Lanternleaf Fried Rice</span><span class="desc">Shrimp, chicken and beef, farm fresh eggs, onions and scallions</span></span><span class="price">$12</span></div>
    <div class="item"><span class="txt"><span class="name">Vegetarian White Fried Rice</span><span class="desc">Mixed vegetables with white rice</span></span><span class="price">$10</span></div>
    <div class="item"><span class="txt"><span class="name">Lanternleaf Lo Mein</span><span class="desc">Shrimp, chicken and beef, farm fresh eggs, onions and scallions</span></span><span class="price">$12</span></div>
    <div class="item"><span class="txt"><span class="name">Vegetarian Lo Mein</span><span class="desc">Mixed vegetables with lo mein noodles</span></span><span class="price">$10</span></div>
    <h2 class="h-section">Vegetarian Dishes</h2>
    <div class="item"><span class="txt"><span class="name">Wok Tossed String Beans <i class="hot"></i></span><span class="desc">Fresh string beans mixed with pickled vegetables</span></span><span class="price">$9</span></div>
    <div class="item"><span class="txt"><span class="name">Mapo Tofu <i class="hot"></i><i class="hot"></i></span><span class="desc">Soft tofu, scallion, Sichuan peppercorn and peppers</span></span><span class="price">$11</span></div>
    <div class="item"><span class="txt"><span class="name">Spicy Garlic Eggplant <i class="hot"></i></span><span class="desc">Chinese eggplant in spicy garlic sauce drizzled with scallions</span></span><span class="price">$12</span></div>
    <div class="item"><span class="txt"><span class="name">Buddha's Delight</span><span class="desc">Seasonal vegetables wok tossed in our light soy garlic sauce</span></span><span class="price">$10</span></div>
    <div class="item"><span class="txt"><span class="name">Stir Fried Eggplant Beans <i class="hot"></i></span><span class="desc">Chinese eggplant with sauteed green beans</span></span><span class="price">$12</span></div>
    <div class="item"><span class="txt"><span class="name">Shiitake Baby Bok Choy</span><span class="desc">Sauteed baby bok choy with shiitake mushrooms in brown sauce</span></span><span class="price">$12</span></div>
    <h2 class="h-section">Kids Menu</h2>
    <div class="item"><span class="txt"><span class="name">Beef Lo Mein</span><span class="desc">Lo mein noodles mixed with beef in garlic sauce</span></span><span class="price">$5</span></div>
    <div class="item"><span class="txt"><span class="name">Chicken Fried Rice</span><span class="desc">Fried rice, farm fresh eggs, onions and scallions</span></span><span class="price">$5</span></div>
    <div class="item"><span class="txt"><span class="name">Sweet &amp; Sour Chicken</span><span class="desc">Bite sized crispy chicken with sweet &amp; sour sauce</span></span><span class="price">$6</span></div>
    <div class="item"><span class="txt"><span class="name">Lemon Chicken</span><span class="desc">Bite sized crispy chicken in a sweet lemon sauce</span></span><span class="price">$6</span></div>
  </div>

  <div class="panel bar compact">
    <h2 class="h-section">Desserts</h2>
    <div class="item"><span class="txt"><span class="name">The Great Wall of Cake</span><span class="desc">Scale this fortress of chocolate cake delight</span></span><span class="price">$7</span></div>
    <div class="item"><span class="txt"><span class="name">Cheesecake Wontons (4)</span><span class="desc">Fried wontons stuffed with cheesecake, dipped in raspberry sauce</span></span><span class="price">$6</span></div>
    <div class="item"><span class="txt"><span class="name">Tempura Snowball</span><span class="desc">Vanilla ice cream fried in tempura batter with powdered sugar and fudge</span></span><span class="price">$4</span></div>
    <div class="item"><span class="txt"><span class="name">Sweet Rice Patties in Caramel</span><span class="desc">Traditional Chinese dessert with sweet rice dipped in a caramel sauce</span></span><span class="price">$7</span></div>
    <h2 class="h-section">Lantern Bar Menu</h2>
    <h3 class="h-sub">Beer</h3>
    <div class="bar-cols">
      <div><b>Domestic $3</b>Heron Light<br>Cane Row Lager<br>Oakline Light<br>Marigold Ultra<br>Porchlight Lite<br>Saltmarsh Amber</div>
      <div><b>Domestic $4</b>Redbud Amber<br>Sugarmill Wheat<br>Gulf Porch Pale<br>Harvest Lantern</div>
      <div><b>Imports $4</b>Playa Azul<br>Windmill Gold<br>Lumen Pils<br>Snowcrest Premium<br>Jade Tiger<br>First Crane</div>
      <div><b>N/A Beer $3</b>Clearwater Zero</div>
    </div>
    <h3 class="h-sub">Wines</h3>
    <div class="bar-cols">
      <div style="flex:1.3"><b>White</b>Alder Creek Chardonnay $7<br>Quill Hill Chardonnay $8<br>Fennel Row Pinot Grigio $6<br>Maple Lane Pinot Gris $8<br>Tidewater Sauv. Blanc $7<br>Lark Cove Sauv. Blanc $9<br>Stonebrook Riesling $6<br>Dolcetta Moscato $7<br><b>Sake</b>Moonriver (Hot) $5<br>Ink &amp; Gold (Hot) $10<br>Pear (Cold) $8<br>Plum (Cold) $8<br>Lychee (Cold) $8</div>
      <div style="flex:1.3"><b>Reds</b>Alder Creek Cabernet $7<br>Copper Ridge Cabernet $9<br>Misty Hollow Merlot $9<br>Lantern Hill Pinot Noir $7<br>Shell Cove Pinot Noir $8<br>Seven Vows Red Blend $7<br>Hollybrook White Zin $5<br><b>House Wine</b>Chardonnay $6<br>Cabernet $6<br>Merlot $6</div>
      <div><b>Sparkling</b>Brightwell Brut $6<br>Verdello Prosecco $6<br>Maison Clair Brut $45</div>
    </div>
    <h3 class="h-sub">Speciality Cocktails</h3>
    <div class="item"><span class="txt"><span class="name">Sake Tini Drop</span><span class="desc">House rice vodka mixed with Asian pear sake, simple syrup and sour mix</span></span><span class="price">$9</span></div>
    <div class="item"><span class="txt"><span class="name">Raz/Pom Martini</span><span class="desc">Raspberry vodka with a pomegranate liqueur and sour mix</span></span><span class="price">$8</span></div>
    <div class="item"><span class="txt"><span class="name">Lemon Ginger Drop Martini</span><span class="desc">Citrus vodka, ginger vodka, ginger zest and sour mix</span></span><span class="price">$8</span></div>
    <div class="item"><span class="txt"><span class="name">Lotus Blossom</span><span class="desc">House vodka, sparkling sake with lychee nuts and simple syrup</span></span><span class="price">$9</span></div>
    <div class="item"><span class="txt"><span class="name">Beijing Fashioned</span><span class="desc">Rye whiskey and plum bitters with simple syrup, orange &amp; black cherries</span></span><span class="price">$9</span></div>
    <div class="item"><span class="txt"><span class="name">Samurai Smash</span><span class="desc">Bourbon whiskey with black cherry puree, sour mix and lemon</span></span><span class="price">$9</span></div>
    <div class="item"><span class="txt"><span class="name">Cosmic Mandarin</span><span class="desc">Orange vodka with orange liqueur, cranberry juice and sour mix</span></span><span class="price">$6</span></div>
    <div class="item"><span class="txt"><span class="name">Lanternleaf Bloody Mary</span><span class="desc">A specially blended Asian infused vodka with a spicy Bloody Mary mix</span></span><span class="price">$6</span></div>
    <div class="item"><span class="txt"><span class="name">Cucumber Smash</span><span class="desc">Dry gin, simple syrup, sour mix with cucumber slices and fresh mint</span></span><span class="price">$9</span></div>
    <div class="item"><span class="txt"><span class="name">Sake Mojito</span><span class="desc">White rum with sake, a splash of lime juice and fresh mint</span></span><span class="price">$9</span></div>
    <div class="item"><span class="txt"><span class="name">Top Shelf Margarita</span><span class="desc">Silver tequila with orange liqueur, rita mix and orange cognac float</span></span><span class="price">$10</span></div>
  </div>
</section>

</body>
</html>
```